VORLEN Website Design

We need a website designed for our company VORLEN. We are a luxury lifestyle club that will provide benefits and services for our members. The site should be clean & sleek, preferably using black and white (or darker colors). (example sites: brimvale.example, tusko.example)

Here is a link of a sample page I did using wix. (https://pelmundry4.sitebuild.example/mypage) This can be used to get a general idea.

Target Market(s)

Upper Middle Class in the United States

Number of Pages Required

5+ page

Font styles to use
Sans Serif
Other font styles liked:
• Arial (or other similar fonts)

Requirements
Must have
• A clean design that is eye-catching and speaks to our company.
Nice to have
• Ideas for copy.

```html
<!DOCTYPE html>
<html lang="en">
<head>
<meta charset="utf-8">
<title>VORLEN — A Members Only Lifestyle Club</title>
<link href="https://fonts.googleapis.com/css2?family=Arimo:wght@400;700&display=swap" rel="stylesheet">
<style>
  :root {
    --header-bg: #e3e3e3;
    --ink: #111111;
    --ink-soft: #555555;
    --paper: #ffffff;
    --night: #000000;
    --night-soft: #1a1a1a;
    --footer-bg: #0c0c0c;
    --button: #8a8a8a;
    --button-text: #f2f2f2;
    --muted: #bdbdbd;
    --footer-muted: #5a5a5a;
  }
  * { box-sizing: border-box; margin: 0; padding: 0; }
  html, body { width: 670px; height: 1200px; overflow: hidden; }
  body {
    position: relative;
    background: var(--paper);
    font-family: "Arimo", Arial, sans-serif;
    color: var(--ink);
  }
  .abs { position: absolute; }

  /* Header */
  .site-header { left: 0; top: 0; width: 670px; height: 41px; background: var(--header-bg); }
  .brand { left: 64px; top: 12px; font-size: 17px; letter-spacing: 0.3px; color: var(--ink); }
  .nav-item { top: 15px; font-size: 7.5px; color: #333; }
  .nav-home {
    left: 434px; top: 10px; width: 41px; height: 18px;
    border: 1px solid #9a9a9a; border-radius: 4px; background: #d6d6d6;
    display: flex; align-items: center; justify-content: center;
  }
  .nav-about { left: 490px; }
  .nav-services { left: 528px; }

  /* Hero */
  .hero {
    left: 0; top: 41px; width: 670px; height: 257px;
    background: linear-gradient(110deg, #6e6e6e 0%, #4a4a4a 35%, #3a3a3a 60%, #111 85%, #050505 100%);
  }
  .hero-caption-band {
    left: 0; top: 246px; width: 670px; height: 52px;
    background: rgba(20,20,20,0.55);
  }
  .hero-title { left: 64px; top: 260px; font-size: 19px; color: #fff; }

  /* Buttons */
  .btn {
    width: 90px; height: 24px; background: var(--button); color: var(--button-text);
    font-size: 8px; display: flex; align-items: center; justify-content: center;
  }

  /* About */
  .about-photo {
    left: 64px; top: 335px; width: 217px; height: 186px;
    background: linear-gradient(135deg, #9c9c9c, #6a6a6a 55%, #bdbdbd);
  }
  .about-heading { left: 335px; top: 387px; font-size: 12px; color: var(--ink-soft); }
  .about-heading strong { font-size: 15px; color: var(--ink); font-weight: 700; margin-left: 2px; }
  .about-copy {
    left: 335px; top: 421px; width: 270px; font-size: 7.8px; line-height: 15.6px; color: #333;
  }
  .about-btn { left: 334px; top: 497px; }

  /* Benefits */
  .benefits-band { left: 0; top: 615px; width: 670px; height: 214px; background: var(--night); }
  .benefits-shadow { left: 0; top: 595px; width: 348px; height: 209px; background: var(--night-soft); }
  .benefits-photo {
    left: 0; top: 566px; width: 336px; height: 214px;
    background: linear-gradient(180deg, #c9c9c9 0%, #a8a8a8 50%, #555 100%);
  }
  .benefits-heading { left: 388px; top: 645px; font-size: 13px; color: #fff; letter-spacing: 0.2px; }
  .benefits-copy { left: 389px; top: 676px; width: 225px; font-size: 7px; line-height: 9.4px; color: var(--muted); }
  .benefits-copy p + p { margin-top: 9px; }
  .benefits-btn { left: 390px; top: 781px; }

  /* Experiences */
  .exp-heading { left: 64px; top: 907px; font-size: 15px; color: var(--ink); }
  .exp-copy { left: 64px; top: 947px; width: 240px; font-size: 7.8px; line-height: 10.4px; color: var(--ink-soft); }
  .exp-copy p + p { margin-top: 8px; }
  .exp-btn { left: 65px; top: 1038px; }
  .exp-photo {
    left: 334px; top: 876px; width: 271px; height: 202px;
    background: radial-gradient(ellipse at 60% 20%, #bdbdbd 0%, #6a6a6a 45%, #2a2a2a 100%);
  }

  /* Footer */
  .site-footer { left: 0; top: 1125px; width: 670px; height: 75px; background: var(--footer-bg); }
  .social { top: 1148px; }
  .contact-btn {
    left: 280px; top: 1148px; width: 109px; height: 25px;
    border: 1px solid #8a8a8a; color: #cfcfcf; font-size: 8px;
    display: flex; align-items: center; justify-content: center;
  }
  .copyright { right: 65px; top: 1156px; font-size: 7px; color: var(--footer-muted); }
</style>
</head>
<body>

  <header class="abs site-header"></header>
  <div class="abs brand">VORLEN</div>
  <nav>
    <div class="abs nav-item nav-home">Home</div>
    <div class="abs nav-item nav-about">About</div>
    <div class="abs nav-item nav-services">Services and Benefits</div>
  </nav>

  <section>
    <div class="abs hero" role="img" aria-label="Black and white photo of friends raising cocktail glasses in a toast"></div>
    <div class="abs hero-caption-band"></div>
    <h1 class="abs hero-title" style="font-weight:400">A Members Only Lifestyle Club</h1>
  </section>

  <section>
    <div class="abs about-photo" role="img" aria-label="Black and white photo of members laughing together at a party"></div>
    <h2 class="abs about-heading" style="font-weight:400">About <strong>VORLEN</strong></h2>
    <p class="abs about-copy">VORLEN is a members only lifestyle club founded in order to bring the best services, experiences, and opportunities to our diverse community of members. Our members consist of creatives, athletes, artists, and other professionals.</p>
    <div class="abs btn about-btn">Learn More</div>
  </section>

  <section>
    <div class="abs benefits-band"></div>
    <div class="abs benefits-shadow"></div>
    <div class="abs benefits-photo" role="img" aria-label="Black and white photo of travellers stepping off a private jet onto the runway"></div>
    <h2 class="abs benefits-heading" style="font-weight:400">BENEFITS AND SERVICES</h2>
    <div class="abs benefits-copy">
      <p>VORLEN membership provides you with amazing benefits and services.</p>
      <p>Members receive access to the best accountants, attorneys, real estate agents, private bankers/advisers and more.</p>
      <p>VORLEN members also receive access to private flight travel, premium luxury gym memberships, private social clubs, and private investment opportunities.</p>
    </div>
    <div class="abs btn benefits-btn">Learn More</div>
  </section>

  <section>
    <h2 class="abs exp-heading" style="font-weight:400">Experiences</h2>
    <div class="abs exp-copy">
      <p>VORLEN organizes and supports a ton of private events and parties for our members.</p>
      <p>Members are also provided access to exclusive venues and events from our partners.</p>
      <p>Network with other members to build lasting relationships.</p>
    </div>
    <div class="abs btn exp-btn">Learn More</div>
    <div class="abs exp-photo" role="img" aria-label="Black and white photo of a crowd dancing with raised hands at a concert"></div>
  </section>

  <footer class="abs site-footer"></footer>
  <svg class="abs social" style="left:63px" width="130" height="24" viewBox="0 0 130 24" aria-label="Social links">
    <g fill="none" stroke="#6a6a6a" stroke-width="1">
      <circle cx="12" cy="12" r="11"/>
      <circle cx="46" cy="12" r="11"/>
      <circle cx="80" cy="12" r="11"/>
      <circle cx="115" cy="12" r="11"/>
    </g>
  </svg>
  <div class="abs contact-btn">Contact Us</div>
  <div class="abs copyright">© 2018 by Brightmere Studio.</div>

</body>
</html>
```